Business Card Design and Basic Text Logo

We are looking for a business card design for an e-business company. Our business is the parent company of a few website businesses. The final logo and business card design will communicate a conservative but modern and expansive business

The Logo text is: 87Merchant
We would also like a basic text logo design for 87Merchant. The logo could also fill up the reverse side of the business card.

The colours we would like to use are:
White
Navy
Black

This is the text that will be added to the card:

Dean Colley
Business Development Manager

Phone: +61 417 658 294
Email: dean.colley@87merchant.com.au

Industry/Entity Type

Business

Logo Text

87Merchant

Logo styles of interest
Pictorial/Combination Logo
Requirements
Must have
• Modern and attractive design
Nice to have
• communicate a conservative but modern and expansive business
Should not have
• Should be too dull and plan
• But also should be overly colourful

```html
<!DOCTYPE html>
<html lang="en">
<head>
<meta charset="utf-8">
<title>87Merchant Business Card</title>
<link rel="stylesheet" href="https://fonts.googleapis.com/css2?family=Mulish:wght@500&family=Tinos:wght@400;700&display=swap">
<style>
  :root {
    --paper: #ffffff;
    --navy: #0505a8;
    --ink: #17181a;
    --reverse-text: #ffffff;
  }
  html, body {
    margin: 0;
    padding: 0;
    width: 1200px;
    height: 939px;
    overflow: hidden;
    background: var(--paper);
  }
  .card-spread {
    position: relative;
    width: 1200px;
    height: 939px;
    overflow: hidden;
  }
  .card-front {
    position: absolute;
    left: 0;
    top: 0;
    width: 601px;
    height: 939px;
    background: var(--paper);
    color: var(--ink);
  }
  .wordmark {
    position: absolute;
    left: 46px;
    top: 168px;
    margin: 0;
    font-family: "Mulish", sans-serif;
    font-weight: 500;
    font-size: 94px;
    letter-spacing: -2px;
    line-height: 1;
    color: var(--ink);
  }
  .contact {
    position: absolute;
    left: 55px;
    font-family: "Tinos", "Times New Roman", serif;
    color: var(--ink);
  }
  .contact-name {
    top: 480px;
    margin: 0;
    font-weight: 700;
    font-size: 27px;
    line-height: 1.2;
  }
  .contact-role {
    top: 514px;
    margin: 0;
    font-weight: 400;
    font-size: 26px;
    line-height: 1.2;
  }
  .contact-details {
    top: 588px;
    margin: 0;
    padding: 0;
    list-style: none;
    font-size: 21px;
    line-height: 27.5px;
  }
  .legal {
    position: absolute;
    left: 55px;
    top: 820px;
    margin: 0;
    font-family: "Tinos", "Times New Roman", serif;
    font-size: 17.5px;
    line-height: 23px;
    color: var(--ink);
  }
  .card-back {
    position: absolute;
    left: 601px;
    top: 0;
    width: 599px;
    height: 939px;
    background: var(--navy);
    overflow: hidden;
  }
  .back-wordmark {
    position: absolute;
    left: 150px;
    top: 130px;
    margin: 0;
    font-family: "Mulish", sans-serif;
    font-weight: 500;
    font-size: 560px;
    line-height: 1;
    letter-spacing: -12px;
    white-space: nowrap;
    color: var(--reverse-text);
  }
</style>
</head>
<body>
  <main class="card-spread">
    <section class="card-front">
      <p class="wordmark">87Merchant</p>

      <p class="contact contact-name">Dean Colley</p>
      <p class="contact contact-role">Business Development Manager</p>

      <ul class="contact contact-details">
        <li>e: dean.colley@87merchant.com.au</li>
        <li>p: +61 417 658 294</li>
        <li>w: 87merchant.com.au</li>
      </ul>

      <p class="legal">
        87Merchant e-businesses Pty Ltd<br>
        Registered office: 512 Harbour Lane, Melbourne VIC 3870<br>
        Registered in Australia under Number: AU618093
      </p>
    </section>

    <section class="card-back">
      <p class="back-wordmark" aria-label="87Merchant">87Merchant</p>
    </section>
  </main>
</body>
</html>
```